Powerpoint template & style design project

KLavender Consulting is an IT technology firm specializing in mobility and telecommunications applications. We provide technical consulting to global companies that want to build mobile applications and take critical business applications and move them into the cloud.
We would like to see designs that use the color blue. The final design should communicate confidence, agility and speak to technology focused customers. Forward progress and/or motion should be conveyed.

Target Market(s)

Government customers and large enterprise companies

Industry/Entity Type

Telecommunications

Font styles to use
Sans Serif

Colors
0555a3

Requirements
Must have
• different slides: Cover page, title slide, main content, transition slide, close out slide..

```html
<!DOCTYPE html>
<html lang="en">
<head>
<meta charset="utf-8">
<title>KLavender Consulting – Presentation Template</title>
<link href="https://fonts.googleapis.com/css2?family=Open+Sans:ital,wght@0,400;0,600;0,700;0,800;1,700&display=swap" rel="stylesheet">
<style>
:root{
  --brand:#0555a3;
  --brand-dark:#034a8f;
  --ink:#4a4a4a;
  --muted:#777;
  --stage:#2b2b2b;
  --white:#fff;
  --green:#9bbb59;
  --mid-blue:#2e86c8;
  --navy:#263a55;
  --ring:#d4d4d4;
  --ring-dark:#444;
}
*{box-sizing:border-box;margin:0;padding:0}
html,body{width:1000px;height:1200px;overflow:hidden}
body{background:var(--stage);font-family:"Open Sans",Arial,sans-serif;color:var(--ink);position:relative}
.slide{position:absolute;width:457px;height:341px;background:var(--white);overflow:hidden}
.s1{left:28px;top:57px}.s2{left:515px;top:57px}
.s3{left:28px;top:431px}.s4{left:515px;top:431px}
.s5{left:28px;top:802px}.s6{left:515px;top:802px}

.header{position:absolute;left:0;top:0;width:100%;height:52px;background:var(--brand);color:var(--white);padding:9px 0 0 13px}
.header::after{content:"";position:absolute;left:74px;bottom:-6px;border:6px solid transparent;border-bottom:0;border-top-color:var(--brand)}
.header h2{font-size:17px;font-weight:700;line-height:19px;letter-spacing:.2px}
.header p{font-size:12.5px;line-height:14px}

.footer{position:absolute;left:0;bottom:0;width:100%;height:9px;background:var(--brand)}
.page-no{position:absolute;right:10px;bottom:0;font-size:5px;color:var(--white);line-height:9px}
.mark{position:absolute;right:28px;bottom:16px;font-size:7.5px;font-weight:700;color:var(--brand);display:flex;align-items:center;gap:3px}
.mark .dot{width:6px;height:6px;background:var(--brand)}

.cover-top{position:absolute;left:0;top:0;width:100%;height:101px}
.cover-top::after{content:"";position:absolute;left:106px;bottom:-6px;border:6px solid transparent;border-bottom:0;border-top-color:var(--white);z-index:2}
.cover-logo{position:absolute;left:20px;top:50px;font-size:17px;font-weight:700;color:var(--brand);display:flex;align-items:center;gap:6px}
.cover-logo .dot{width:14px;height:14px;background:var(--brand)}
.cover-body{position:absolute;left:0;top:101px;width:100%;height:240px;background:var(--brand);color:var(--white);padding:64px 0 0 21px}
.cover-body h1{font-size:20px;font-weight:700;line-height:26px}
.cover-body .sub{font-size:14px;line-height:20px}
.cover-body .date{font-size:14px;margin-top:16px}

.photo{position:absolute;background:linear-gradient(90deg,#2c6cb0,#5b8fc7 45%,#3f79b9 70%,#2a66aa)}
.s2 .photo{left:15px;top:101px;width:427px;height:143px}
.body-text{position:absolute;font-size:8.2px;line-height:12.5px;color:var(--ink)}
.s2 .body-text{left:15px;top:252px;width:218px;text-align:justify}

.quote{position:absolute;left:18px;top:83px;width:110px;font-size:6.2px;line-height:9.2px;font-weight:700;font-style:italic;color:var(--brand);text-align:justify}
.col{position:absolute;top:83px;width:141px;font-size:5.6px;line-height:9.2px;color:var(--muted);text-align:justify}
.col p+p{margin-top:9px;text-indent:10px}
.col p:first-child{text-indent:10px}
.col-a{left:147px}.col-b{left:300px}

.chart{position:absolute}
.divider{position:absolute;left:233px;top:80px;width:1px;height:190px;background:#e2e2e2}
.cap{position:absolute;width:180px}
.cap h3{font-size:9px;font-weight:400;color:var(--ink);margin-bottom:4px}
.cap p{font-size:6.3px;line-height:8.4px;color:var(--ink);text-align:justify}
.legend{position:absolute;font-size:6px;line-height:11px;color:var(--ink)}
.legend span{display:inline-block;width:5px;height:5px;margin-right:3px}

.section-bg{position:absolute;inset:0;background:radial-gradient(circle at 55% 45%,#3a78bb,#1f5fa6 60%,#175499)}
.section-ring{position:absolute;left:172px;top:120px}
.section-label{position:absolute;left:172px;top:158px;width:112px;text-align:center;color:var(--white);font-size:13px;font-weight:700;line-height:16px}
.s5 .mark{color:var(--white)}
.s5 .mark .dot{background:var(--white)}

.thanks{position:absolute;left:13px;top:88px;font-size:33px;font-weight:800;color:var(--brand);letter-spacing:.5px}
.contact{position:absolute;font-size:10px;line-height:14px;color:var(--brand);list-style:none}
.contact li{display:flex;gap:8px;align-items:flex-start}
.contact svg{flex:none;margin-top:1px}
.contact-left{left:13px;top:155px;width:200px}
.contact-left li+li{margin-top:16px}
.contact-right{left:243px;top:155px}
.contact-right li+li{margin-top:14px}
.close-band{position:absolute;left:0;bottom:0;width:100%;height:51px;background:var(--brand)}
.close-band .mark{right:22px;bottom:16px;font-size:11px;color:var(--white)}
.close-band .mark .dot{width:9px;height:9px;background:var(--white)}
</style>
</head>
<body>

<section class="slide s1">
  <div class="cover-top">
    <div class="cover-logo"><span class="dot"></span>KLavender Consulting</div>
  </div>
  <div class="cover-body">
    <h1>Insert The Title of Your<br>Presentation Here</h1>
    <p class="sub">Subtitle of the Presentation</p>
    <p class="date">April 12, 2015</p>
  </div>
</section>

<section class="slide s2">
  <header class="header"><h2>INTRODUCTION</h2><p>About Us</p></header>
  <div class="photo" role="img" aria-label="Blue-tinted photo of a business handshake in front of a city skyline"></div>
  <p class="body-text">Lorem ipsum dolor sit amet, consectetur adipiscing elit, sed do eiusmod tempor incididunt ut labore et dolore magna aliqua. Ut enim ad minim veniam, quis nostrud exercitation ullamco laboris nisi ut aliquip.</p>
  <div class="mark"><span class="dot"></span>KLavender Consulting</div>
  <div class="footer"><span class="page-no">2</span></div>
</section>

<section class="slide s3">
  <header class="header"><h2>YOUR SAMPLE TITLE</h2><p>Your subtitle goes here</p></header>
  <p class="quote">"Sed ut perspiciatis unde omnis iste natus error sit voluptatem accusantium doloremque laudantium, totam rem aperiam, eaque ipsa quae ab illo inventore veritatis et quasi architecto beatae vitae"</p>
  <div class="col col-a">
    <p>Lorem ipsum dolor sit amet, consectetur adipiscing elit sed do eiusmod tempor incididunt ut labore et dolore magna aliqua. Ut enim ad minim veniam, quis nostrud exercitation ullamco laboris nisi ut aliquip ex ea commodo consequat. Duis aute irure dolor in reprehenderit in voluptate velit esse cillum dolore eu fugiat nulla pariatur. Excepteur sint occaecat cupidatat non proident, sunt in culpa qui mollit anim id est laborum.</p>
    <p>Sed ut perspiciatis unde omnis iste natus error sit voluptatem accusantium doloremque laudantium, totam rem aperiam, eaque ipsa quae ab illo inventore veritatis et quasi architecto beatae vitae dicta sunt explicabo. Nemo enim ipsam voluptatem quia voluptas sit aspernatur</p>
  </div>
  <div class="col col-b">
    <p>aut odit aut fugit, sed quia consequuntur magni dolores eos qui ratione voluptatem sequi nesciunt. Neque porro quisquam est, qui dolorem ipsum quia dolor sit amet, consectetur, adipisci velit, sed quia non numquam eius modi tempora incidunt ut labore et dolore magnam aliquam quaerat voluptatem. Ut enim ad minima veniam, quis nostrum exercitationem ullam corporis suscipit laboriosam, nisi ut aliquid ex ea commodi consequatur?</p>
    <p>Quis autem vel eum iure reprehenderit qui in ea voluptate velit esse quam nihil molestiae consequatur, vel illum qui dolorem eum fugiat quo voluptas nulla pariatur? At vero eos et</p>
  </div>
  <div class="mark"><span class="dot"></span>KLavender Consulting</div>
  <div class="footer"><span class="page-no">3</span></div>
</section>

<section class="slide s4">
  <header class="header"><h2>YOUR SAMPLE TITLE</h2><p>Your subtitle goes here</p></header>
  <svg class="chart" style="left:16px;top:88px" width="160" height="115" viewBox="0 0 160 115" font-family="Open Sans, sans-serif" font-size="5" fill="#555">
    <g stroke="#e6e6e6" stroke-width=".5">
      <line x1="22" y1="4" x2="158" y2="4"/><line x1="22" y1="24" x2="158" y2="24"/><line x1="22" y1="44" x2="158" y2="44"/><line x1="22" y1="64" x2="158" y2="64"/><line x1="22" y1="84" x2="158" y2="84"/>
    </g>
    <line x1="22" y1="104" x2="158" y2="104" stroke="#bbb" stroke-width=".6"/>
    <g text-anchor="end"><text x="16" y="6">5</text><text x="16" y="26">4</text><text x="16" y="46">3</text><text x="16" y="66">2</text><text x="16" y="86">1</text><text x="16" y="106">0</text></g>
    <rect x="30" y="18" width="10" height="86" fill="#9bbb59"/><rect x="40" y="56" width="10" height="48" fill="#2e86c8"/><rect x="50" y="64" width="10" height="40" fill="#263a55"/>
    <rect x="76" y="54" width="10" height="50" fill="#9bbb59"/><rect x="86" y="16" width="10" height="88" fill="#2e86c8"/><rect x="96" y="64" width="10" height="40" fill="#263a55"/>
    <rect x="122" y="34" width="10" height="70" fill="#9bbb59"/><rect x="132" y="68" width="10" height="36" fill="#2e86c8"/><rect x="142" y="44" width="10" height="60" fill="#263a55"/>
    <g text-anchor="middle"><text x="45" y="113">Category 1</text><text x="91" y="113">Category 2</text><text x="137" y="113">Category 3</text></g>
  </svg>
  <div class="legend" style="left:180px;top:130px">
    <div><span style="background:var(--green)"></span>Series 1</div>
    <div><span style="background:var(--mid-blue)"></span>Series 2</div>
    <div><span style="background:var(--navy)"></span>Series 3</div>
  </div>
  <div class="cap" style="left:44px;top:213px"><h3>Chart Sample One</h3><p>Lorem ipsum dolor sit amet, consectetur adipiscing elit. Aliquam tincidunt ante nec sem congue convallis lorem ipsum.</p></div>
  <div class="divider"></div>
  <svg class="chart" style="left:270px;top:90px" width="100" height="100" viewBox="0 0 100 100">
    <path d="M50 50 L50 0 A50 50 0 0 1 58.7 99.2 Z" fill="#9bbb59"/>
    <path d="M50 50 L58.7 99.2 A50 50 0 0 1 1.7 62.9 Z" fill="#2e86c8"/>
    <path d="M50 50 L1.7 62.9 A50 50 0 0 1 50 0 Z" fill="#263a55"/>
  </svg>
  <div class="legend" style="left:388px;top:130px">
    <div><span style="background:var(--green)"></span>Category 1</div>
    <div><span style="background:var(--mid-blue)"></span>Category 2</div>
    <div><span style="background:var(--navy)"></span>Category 3</div>
  </div>
  <div class="cap" style="left:270px;top:213px;width:156px"><h3>Chart Sample Two</h3><p>Lorem ipsum dolor sit amet, consectetur adipiscing elit. Aliquam tincidunt ante nec sem congue convallis lorem ipsum.</p></div>
  <div class="mark"><span class="dot"></span>KLavender Consulting</div>
  <div class="footer"><span class="page-no">4</span></div>
</section>

<section class="slide s5">
  <div class="section-bg" role="img" aria-label="Blue-tinted photo of a laptop and a coffee cup on a desk"></div>
  <svg class="section-ring" width="112" height="112" viewBox="0 0 112 112">
    <circle cx="56" cy="56" r="48" fill="none" stroke="var(--ring)" stroke-width="10"/>
    <circle cx="56" cy="56" r="48" fill="none" stroke="var(--ring-dark)" stroke-width="10" stroke-dasharray="75.4 226.2" transform="rotate(-90 56 56)"/>
  </svg>
  <p class="section-label">SECTION<br>TWO</p>
  <div class="mark"><span class="dot"></span>KLavender Consulting</div>
</section>

<section class="slide s6">
  <header class="header"><h2>YOUR SAMPLE TITLE</h2><p>Your subtitle goes here</p></header>
  <h2 class="thanks">THANK YOU</h2>
  <ul class="contact contact-left">
    <li><svg width="10" height="13" viewBox="0 0 10 13"><path d="M5 0a5 5 0 0 0-5 5c0 3.5 5 8 5 8s5-4.5 5-8a5 5 0 0 0-5-5z" fill="var(--brand)"/><circle cx="5" cy="5" r="2" fill="#fff"/></svg><span>Lorem ipsum dolor sit amet, consectetur adipiscing elit, sed do eiusmod tempor incididunt ut labore et dolore</span></li>
    <li><svg width="11" height="11" viewBox="0 0 24 24"><path d="M6.6 10.8a15.1 15.1 0 0 0 6.6 6.6l2.2-2.2c.3-.3.7-.4 1-.2 1.1.4 2.3.6 3.6.6.6 0 1 .4 1 1V20c0 .6-.4 1-1 1A17 17 0 0 1 3 4c0-.6.4-1 1-1h3.5c.6 0 1 .4 1 1 0 1.3.2 2.5.6 3.6.1.3 0 .7-.2 1z" fill="var(--brand)"/></svg><span>1234567890</span></li>
  </ul>
  <ul class="contact contact-right">
    <li><svg width="14" height="11" viewBox="0 0 14 11"><rect x=".6" y=".6" width="12.8" height="9.8" fill="none" stroke="var(--brand)" stroke-width="1.2"/><path d="M.6.6 7 6l6.4-5.4" fill="none" stroke="var(--brand)" stroke-width="1.2"/></svg><span>jhon.doe@klavenderconsulting.com</span></li>
    <li><svg width="14" height="12" viewBox="0 0 14 12"><circle cx="6" cy="6" r="5" fill="var(--brand)"/></svg><span>klavenderconsulting</span></li>
    <li><svg width="14" height="12" viewBox="0 0 14 12"><circle cx="6" cy="6" r="5" fill="var(--brand)"/></svg><span>@klavenderconsulting</span></li>
    <li><svg width="14" height="12" viewBox="0 0 14 12"><circle cx="6" cy="6" r="5" fill="none" stroke="var(--brand)" stroke-width="1.2"/><path d="M1 6h10M6 1c-2.5 3-2.5 7 0 10M6 1c2.5 3 2.5 7 0 10" fill="none" stroke="var(--brand)" stroke-width=".9"/></svg><span>www.klavenderconsulting.com</span></li>
  </ul>
  <div class="close-band"><div class="mark"><span class="dot"></span>KLavender Consulting</div></div>
</section>

</body>
</html>
```